IT Product Event Invitations

We are requesting the design of two invitations for a series of technological events that will be held between the company Velto Grid and its partner in the Dominican Republic, Corvanel.
Both events represent the launch of the Velto Grid brand in the Dominican Republic.
The first event is an elegant dinner aimed at the banking sector of the Dominican Republic to showcase the "Ledgerwise Suite" software.
Event information:
- Descriptive text for the invitation: Corvanel y Velto Grid le invitan a descubrir cómo reducir costos, aumentar la automatización y mejorar la satisfacción de los clientes a través de una solución única para enfrentar los desafíos de la banca.
- Date: 25 de Septiembre
- Time: 7PM
- Location: El Miradero, Av. Tomás Herrandez 817
In the invitation, consider using the colors of the Velto Grid and Corvanel brands if possible. You can find the logos in the webpage
The second event is a wine tasting to present "Orbital Desk Platform" aimed at various industries.
Event information:
- Descriptive text for the invitation: Corvanel y Velto Grid le invitan a conocer una solución que le permitirá a toda su empresa brindar una experiencia de servicio a otro nivel.
- Date: 26 de Septiembre
- Time: 7PM
In the invitation, consider using the colors of the Velto Grid and Corvanel brands if possible. You can find the logos in the web page.
Both invitations must have a button for participant registration and that when you click on the image, it will direct you to a form.
Form for Ledgerwise Suite: https://signup.quilvane.example/events/a7Kq2Rm9Xw4Tz1Lp8Vb3Nc6Hd0Jf5Gs
Form for Orbital Desk Platform: https://signup.quilvane.example/events/b3Wd8Yt1Pq6Rn4Ks0Mz7Fc2Lx9Hv5Je

```html
<!DOCTYPE html>
<html lang="es">
<head>
<meta charset="utf-8">
<title>Invitaciones Velto Grid</title>
<link href="https://fonts.googleapis.com/css2?family=Poppins:wght@400;500;600;700;800&family=Mr+Dafoe&family=Josefin+Sans:wght@400;600&display=swap" rel="stylesheet">
<style>
  :root{
    --stage:#b1b1b1;
    --paper:#f1f1f0;
    --sand:#ece4da;
    --ink:#1f1f1f;
    --orange:#f06a22;
    --amber:#f7a335;
    --green:#62c14a;
    --dash:#8d8a86;
  }
  *{margin:0;padding:0;box-sizing:border-box}
  html,body{width:1200px;height:924px;overflow:hidden;background:var(--stage)}
  .stage{position:relative;width:1200px;height:924px}
  .flyer{position:absolute;top:128px;width:458px;height:647px;background:var(--paper);overflow:hidden;
    font-family:"Poppins",sans-serif;color:var(--ink);text-decoration:none;display:block}
  .flyer--dinner{left:117px}
  .flyer--wine{left:626px}
  .photo{position:absolute;left:0;top:150px;width:230px;height:320px;
    background:radial-gradient(ellipse at 40% 50%,rgba(150,150,150,.45),rgba(200,200,200,.15) 60%,rgba(241,241,240,0) 80%)}
  .decor{position:absolute;inset:0}
  .series{position:absolute;top:36px;left:0;width:100%;text-align:center;font-size:10.5px;letter-spacing:3.2px;font-weight:500;text-transform:uppercase}
  .kicker{position:absolute;left:103px;top:62px;padding-top:6px;font-family:"Josefin Sans",sans-serif;font-weight:600;font-size:38px;line-height:1.2;letter-spacing:1px;
    background:linear-gradient(90deg,var(--amber),var(--orange));-webkit-background-clip:text;background-clip:text;color:transparent}
  .script{position:absolute;left:0;top:0;width:458px;height:240px;overflow:visible}
  .script text{font-family:"Mr Dafoe",cursive;font-size:118px;fill:var(--ink)}
  .event-name{position:absolute;top:180px;left:171px;font-size:15.5px;letter-spacing:6.5px;color:var(--orange);font-weight:500;white-space:nowrap}
  .flyer--wine .event-name{left:193px}
  .day{position:absolute;left:175px;top:240px;font-size:96px;font-weight:800;letter-spacing:-4px;line-height:1}
  .day-de{position:absolute;left:280px;top:252px;font-size:9px;font-weight:700;line-height:1;z-index:2}
  .month{position:absolute;left:174px;top:329px;width:106px;height:22px;border-radius:4px;
    background:linear-gradient(90deg,var(--amber),var(--orange));color:#fff;font-weight:600;font-size:15px;text-align:center;line-height:22px}
  .time{position:absolute;left:0;width:456px;top:358px;text-align:center;font-size:13.5px;letter-spacing:.5px}
  .time b{font-weight:700}
  .pin{position:absolute;left:221px;top:393px}
  .venue-label{position:absolute;left:0;width:458px;top:414px;text-align:center;font-size:9.5px;letter-spacing:4.5px}
  .venue{position:absolute;left:0;width:458px;top:425px;text-align:center;font-size:15.5px;font-weight:600;letter-spacing:.2px}
  .copy{position:absolute;left:64px;width:330px;top:474px;text-align:center;font-size:8.3px;line-height:1.27}
  .flyer--wine .copy{top:480px}
  .partners{position:absolute;top:544px;left:0;width:458px;height:28px}
  .partner-a{position:absolute;left:101px;top:4px;display:flex;align-items:center;gap:6px;font-size:16px;font-weight:700}
  .partner-a i{display:block;width:14px;height:14px;border-radius:50%;background:var(--orange)}
  .divider{position:absolute;left:226px;top:0;width:1px;height:26px;background:#bdbdbd}
  .partner-b{position:absolute;left:242px;top:2px;font-size:19px;font-weight:600;letter-spacing:-.3px}
  .register{position:absolute;top:600px;left:104px;height:15px;display:flex;align-items:center;background:rgba(210,200,190,.55);border-radius:8px;padding-right:10px}
  .register-btn{height:15px;padding:0 11px;background:var(--green);border-radius:8px;font-size:8px;font-weight:600;line-height:15px;color:#102a0a;white-space:nowrap}
  .register-url{margin-left:6px;font-size:5.4px;letter-spacing:.1px;white-space:nowrap}
</style>
</head>
<body>
<main class="stage">

  <a class="flyer flyer--dinner" href="https://signup.quilvane.example/events/a7Kq2Rm9Xw4Tz1Lp8Vb3Nc6Hd0Jf5Gs">
    <div class="photo" role="img" aria-label="Faint photo of an elegant dinner table set with glasses"></div>
    <svg class="decor" width="458" height="647" viewBox="0 0 458 647" aria-hidden="true">
      <path d="M130 300 Q140 222 220 222 L458 262 L458 647 L252 647 Z" fill="var(--sand)" opacity=".8"/>
      <path d="M458 148 L335 262 Q300 300 318 340 Q338 380 458 415" fill="none" stroke="var(--dash)" stroke-width=".8" stroke-dasharray="3 3"/>
    </svg>
    <div class="series">Ledgerwise Suite</div>
    <div class="kicker">ESTÁS</div>
    <svg class="script" viewBox="0 0 458 240" aria-label="invitado"><text x="68" y="168" textLength="322" lengthAdjust="spacingAndGlyphs">invitado</text></svg>
    <div class="event-name">NOCHE DE CENA</div>
    <div class="day">25</div><div class="day-de">DE</div>
    <div class="month">SEPTIEMBRE</div>
    <div class="time">TIME - <b>7:00 PM</b></div>
    <svg class="pin" width="12" height="16" viewBox="0 0 12 16" aria-hidden="true"><path d="M6 0a6 6 0 0 1 6 6c0 4-6 10-6 10S0 10 0 6a6 6 0 0 1 6-6z" fill="var(--green)"/><circle cx="6" cy="6" r="2.3" fill="#fff"/></svg>
    <div class="venue-label">VENUE</div>
    <div class="venue">EL MIRADERO, AV. TOMÁS HERRANDEZ 817</div>
    <p class="copy">Corvanel y Velto Grid le invitan a descubrir cómo reducir costos, aumentar la automatización y mejorar la satisfacción de los clientes a través de una solución única para enfrentar los desafíos de la banca.</p>
    <div class="partners">
      <div class="partner-a"><i></i>CORVANEL</div>
      <div class="divider"></div>
      <div class="partner-b">veltogrid</div>
    </div>
    <div class="register"><span class="register-btn">BOOK NOW</span><span class="register-url">https://signup.quilvane.example/events/a7Kq2Rm9Xw4Tz1Lp8Vb3Nc6Hd0Jf5Gs</span></div>
  </a>

  <a class="flyer flyer--wine" href="https://signup.quilvane.example/events/b3Wd8Yt1Pq6Rn4Ks0Mz7Fc2Lx9Hv5Je">
    <div class="photo" role="img" aria-label="Faint photo of a glass of red wine"></div>
    <svg class="decor" width="458" height="647" viewBox="0 0 458 647" aria-hidden="true">
      <path d="M130 300 Q140 222 220 222 L458 262 L458 647 L252 647 Z" fill="var(--sand)" opacity=".8"/>
      <path d="M458 148 L335 262 Q300 300 318 340 Q338 380 458 415" fill="none" stroke="var(--dash)" stroke-width=".8" stroke-dasharray="3 3"/>
    </svg>
    <div class="series">Orbital Desk Platform</div>
    <div class="kicker">ESTÁS</div>
    <svg class="script" viewBox="0 0 458 240" aria-label="invitado"><text x="68" y="168" textLength="322" lengthAdjust="spacingAndGlyphs">invitado</text></svg>
    <div class="event-name">CATA DE VINOS</div>
    <div class="day">26</div><div class="day-de">DE</div>
    <div class="month">SEPTIEMBRE</div>
    <div class="time">TIME - <b>7:00 PM</b></div>
    <svg class="pin" width="12" height="16" viewBox="0 0 12 16" aria-hidden="true"><path d="M6 0a6 6 0 0 1 6 6c0 4-6 10-6 10S0 10 0 6a6 6 0 0 1 6-6z" fill="var(--green)"/><circle cx="6" cy="6" r="2.3" fill="#fff"/></svg>
    <div class="venue-label">VENUE</div>
    <div class="venue">EL MIRADERO, AV. TOMÁS HERRANDEZ 817</div>
    <p class="copy">Corvanel y Velto Grid le invitan a conocer una solución que le permitirá a toda su empresa brindar una experiencia de servicio a otro nivel.</p>
    <div class="partners">
      <div class="partner-a"><i></i>CORVANEL</div>
      <div class="divider"></div>
      <div class="partner-b">veltogrid</div>
    </div>
    <div class="register"><span class="register-btn">BOOK NOW</span><span class="register-url">https://signup.quilvane.example/events/b3Wd8Yt1Pq6Rn4Ks0Mz7Fc2Lx9Hv5Je</span></div>
  </a>

</main>
</body>
</html>
```